Web Design Project

I need designs (PSD only - no programming) for several pages of a new website helping train operators to manage key information about their traindrivers.
The main feature of this website is the management of personnel records (create, edit, search, delete). Another key aspect is the management of user privileges. Since this is a new website we also need a user friendly frontpage, pricing information and how it works sections.
This can be broken down into 9 pages for which we need designs (PSDs).
1. Home
2. Driver record
3. How it works
4. Pricing
5. User administration
6. Help
7. Record list view
8. Login
9. Registration
Navigation (not logged in) are: Home | How it works | Pricing | Customers | About us | Contact
Navigation (logged in) are: Overview | Administration | Manage records | Billing | Help | Contact
Footer: Customer logos | Awards | Terms & Conditions | Privacy
To provide the best support for you to come up with a strong design proposal I will provide DAILY feedback to all participants. We have also created concept mockups (attached) and example pages (below) for each section to give you a clear sense of what we look for.
The core concepts for a successful bid are that the website is EASY to understand, INTUITIVE to navigate, and SIMPLE to use. Most of our users lack technical background and are looking for tool to simplify their work.
The strongest participants (winner and close contenders) will have the opportunity to additional commissioned work on additional sections not included in this brief.
Example Pages (by section)
1. http://www.brovendale.example/site-keepers/
1. http://www.qvt.example/
1. http://www.mondaph.example/
1. http://www.gorvanquest.example/
2. http://www.snapveld.example/profile_edit.gne
3. https://www.tarn.example/how-it-works/
3. http://www.bulkvue.example/learn
4. http://www.pactheron.example/crm/editions-pricing.jsp
4. http://www.brovendale.example/site-keepers/prices
6. https://support.talvora.example/en-gb/
6. http://help.dealmeadow.example/contact_us
8. https://www.careweave.example/uas/login
8. https://www.dealmeadow.example/login
8. http://www.askhollow.example/login/index
For form designs we like Verindo, Bidnook, Snapveld, CareWeave, Chatterly and the concepts presented by Tomas Kerrigan in his classic Layout Craft Shaping the Input Boxes.
For additional guidance see mockups attached!
Target Market(s)
Security, human resources and admin support employees for train operators.
Industry/Entity Type
Learn
Requirements
Should not have
- Home page should not have
Social media icons (chatterly, chirpla, CareWeave, RSS feed)
Contact forms
Read more links
Old trains

```html
<!DOCTYPE html>
<html lang="en">
<head>
<meta charset="utf-8">
<title>Driver Records – Home</title>
<link rel="stylesheet" href="https://fonts.googleapis.com/css2?family=Arimo:wght@400;700&display=swap">
<style>
:root{
  --navy-top:#2b4466;
  --navy-bottom:#1a3150;
  --nav-text:#555;
  --nav-sep:#d4d4d4;
  --heading-blue:#3d6587;
  --accent:#f8ab00;
  --accent-dark:#e69200;
  --body-text:#222;
  --page-blue:#0864b0;
  --icon-grey:#a9a9a9;
}
*{margin:0;padding:0;box-sizing:border-box}
html,body{width:1200px;height:960px;overflow:hidden}
body{font-family:"Arimo",Arial,sans-serif;background:var(--page-blue);position:relative}
.topbar{position:absolute;left:0;top:0;width:1200px;height:45px;background:linear-gradient(var(--navy-top),var(--navy-bottom))}
.account{position:absolute;left:932px;top:15px;font-size:13px;color:#c9d3df;display:flex;align-items:center;gap:6px}
.flag{width:23px;height:12px;margin-left:6px}
.mainnav{position:absolute;left:0;top:45px;width:1200px;height:37px;background:#fff}
.mainnav a{position:absolute;top:10px;font-size:15px;color:var(--nav-text);text-decoration:none;transform:translateX(-50%)}
.mainnav .sep{position:absolute;top:9px;width:1px;height:18px;background:var(--nav-sep)}
.pointer{position:absolute;left:254px;top:82px;z-index:3}
.hero{position:absolute;left:0;top:82px;width:1200px;height:351px;overflow:hidden}
.hero-photo{position:absolute;inset:0;background:linear-gradient(90deg,#6b5a1e 0%,#f4b417 18%,#f7bb1c 45%,#e2a12a 63%,#e8d6a8 78%,#efe5c8 100%)}
.hero-copy{position:absolute;right:11px;top:46px;text-align:right;color:#fff;font-weight:700;font-size:30px;line-height:27px;text-shadow:1px 2px 4px rgba(0,0,0,.7)}
.hero-points{position:absolute;left:820px;top:134px;list-style:none;font-size:16px;color:#111;text-shadow:1px 1px 3px rgba(0,0,0,.45)}
.hero-points li{position:relative;padding-left:28px;height:29px;line-height:22px}
.hero-points li::before{content:"";position:absolute;left:2px;top:4px;width:15px;height:15px;border-radius:50%;background:radial-gradient(circle at 40% 35%,#fff,#c6c6c6)}
.cta{position:absolute;left:895px;top:203px;width:182px;height:43px;border-radius:6px;background:linear-gradient(#fcc21f,var(--accent-dark));color:#fff;font-weight:700;font-size:19px;display:flex;align-items:center;justify-content:center;box-shadow:0 2px 3px rgba(0,0,0,.35)}
.slider-tab{position:absolute;left:495px;top:314px}
.benefits{position:absolute;left:0;top:433px;width:1200px;height:322px;background:#fff;box-shadow:0 6px 14px rgba(0,0,0,.35)}
.benefits h2{position:absolute;left:122px;top:5px;font-size:21px;font-weight:400;color:var(--heading-blue)}
.rule{position:absolute;left:125px;top:29px;width:948px;height:1px;background:#d3d3d3}
.benefit{position:absolute;display:flex;gap:14px}
.benefit svg{flex:none}
.benefit h3{font-size:21px;font-weight:400;color:var(--accent);line-height:22px;margin-top:6px}
.benefit p{font-size:11.5px;color:var(--body-text);line-height:13px;margin-top:2px}
</style>
</head>
<body>
<header class="topbar">
  <div class="account">
    <span>Sign up</span><span>|</span><span>Login |</span>
    <svg class="flag" viewBox="0 0 23 12" aria-label="Language: English"><rect width="23" height="12" fill="#2a3d8f"/><path d="M0 0L23 12M23 0L0 12" stroke="#fff" stroke-width="2.5"/><path d="M0 0L23 12M23 0L0 12" stroke="#c8102e" stroke-width="1"/><path d="M11.5 0V12M0 6H23" stroke="#fff" stroke-width="4"/><path d="M11.5 0V12M0 6H23" stroke="#c8102e" stroke-width="2.2"/></svg>
  </div>
</header>
<nav class="mainnav">
  <a href="#" style="left:263px">Home</a><span class="sep" style="left:314px"></span>
  <a href="#" style="left:395px">How it works</a><span class="sep" style="left:473px"></span>
  <a href="#" style="left:527px">Prices</a><span class="sep" style="left:578px"></span>
  <a href="#" style="left:662px">Our customers</a><span class="sep" style="left:747px"></span>
  <a href="#" style="left:806px">About us</a><span class="sep" style="left:875px"></span>
  <a href="#" style="left:927px">Contact</a>
</nav>
<svg class="pointer" width="18" height="14" viewBox="0 0 18 14"><path d="M0 0H18L9 14Z" fill="#fff"/></svg>
<section class="hero">
  <div class="hero-photo" role="img" aria-label="Yellow modern tram in motion with faint data field overlays, blurred city street behind"></div>
  <div class="hero-copy">Manage your drivers<br>and key information!</div>
  <ul class="hero-points">
    <li>Store, edit , delete and manage your drivers!</li>
    <li>Ultimate management and user privilages</li>
  </ul>
  <div class="cta">Learn More Below</div>
  <svg class="slider-tab" width="210" height="37" viewBox="0 0 210 37">
    <path d="M0 37C18 37 20 0 45 0H165C190 0 192 37 210 37Z" fill="#fff"/>
    <g>
      <circle cx="57" cy="23" r="13" fill="#d7d7d7"/><circle cx="57" cy="22" r="5" fill="#555"/>
      <circle cx="89" cy="23" r="13" fill="#d7d7d7"/><circle cx="89" cy="22" r="5.5" fill="#1a64c8"/>
      <circle cx="120" cy="23" r="13" fill="#d7d7d7"/><circle cx="120" cy="22" r="5" fill="#555"/>
      <circle cx="152" cy="23" r="13" fill="#d7d7d7"/><circle cx="152" cy="22" r="5" fill="#555"/>
    </g>
  </svg>
</section>
<section class="benefits">
  <h2>The Benifits...</h2>
  <div class="rule"></div>
  <div class="benefit" style="left:236px;top:41px">
    <svg width="50" height="50" viewBox="0 0 50 50"><circle cx="25" cy="25" r="25" fill="var(--icon-grey)"/><path d="M14 23h6v13h-6zM22 23l5-9c3 0 3 3 2 7h7c2 0 3 2 2 4l-3 9c-1 2-2 2-4 2H22z" fill="#f4f4f4"/></svg>
    <div><h3>Ease of use</h3><p>Help text, reminders of important dates and events,</p></div>
  </div>
  <div class="benefit" style="left:672px;top:41px">
    <svg width="50" height="50" viewBox="0 0 50 50"><circle cx="25" cy="25" r="25" fill="var(--icon-grey)"/><circle cx="25" cy="25" r="17" fill="none" stroke="#f4f4f4" stroke-width="3" stroke-dasharray="3 5"/><path d="M16 24l7 7 14-17" fill="none" stroke="var(--accent)" stroke-width="5" stroke-linecap="round"/></svg>
    <div><h3>EU Compliant</h3><p>Follows the latest directives</p></div>
  </div>
  <div class="benefit" style="left:236px;top:124px">
    <svg width="50" height="50" viewBox="0 0 50 50"><circle cx="25" cy="25" r="25" fill="var(--icon-grey)"/><path d="M18 23v-5a7 7 0 0 1 14 0v5" fill="none" stroke="#f4f4f4" stroke-width="3"/><rect x="15" y="23" width="20" height="15" rx="2" fill="#f4f4f4"/><circle cx="25" cy="30" r="2.5" fill="var(--icon-grey)"/></svg>
    <div><h3>Safe</h3><p>Securely stored in the cloud</p></div>
  </div>
  <div class="benefit" style="left:672px;top:124px">
    <svg width="50" height="50" viewBox="0 0 50 50"><circle cx="25" cy="25" r="25" fill="var(--icon-grey)"/><circle cx="29" cy="13" r="3.5" fill="#f4f4f4"/><path d="M17 24l6-6h7l-4 9 5 5-2 7M26 27l-6 5-5 2M30 19l4 5 5-1" fill="none" stroke="#f4f4f4" stroke-width="3.5" stroke-linecap="round" stroke-linejoin="round"/></svg>
    <div><h3>Fast</h3><p>Pre-filled fields, logical structure, smart categories,<br>one-click PDF generation</p></div>
  </div>
  <div class="benefit" style="left:236px;top:209px">
    <svg width="50" height="50" viewBox="0 0 50 50"><circle cx="25" cy="25" r="25" fill="var(--icon-grey)"/><g fill="none" stroke="#f4f4f4" stroke-width="2"><circle cx="25" cy="25" r="15"/><ellipse cx="25" cy="25" rx="7" ry="15"/><path d="M10 25h30M13 17h24M13 33h24M25 10v30"/></g></svg>
    <div><h3>Accessible</h3><p>Storage allow easy access from anywhere and privilege<br>&nbsp;rights&nbsp; across&nbsp; different users&nbsp; allows collaborative work</p></div>
  </div>
</section>
</body>
</html>
```